Skill Up Salary Up

Full Page
7.5 w x 10 h / 8 w x 10.75 h + .25" bleed
Full-Page Career Course Ad
Project Overview
• Goal: Create a visually attractive, modern, and uncluttered full-page magazine advertisement to list available career courses.
• Tone: Creative, professional, and attention-grabbing to prevent the reader from turning the page. The final design must prioritize readability.

Content Requirements
1. Header/Headline: Must be the primary focus. And grab peoples attention
2. Course Listing: A clear, well-organized list of the career courses.
________________________________________
Design & Aesthetic Directives
1. Layout & Readability (Crucial)
• The final ad must not look crowded or busy.
• Prioritize white space to make the text "breathe" and ensure the course list is easy to scan and read.
• Use a modern, clean, and professional typeface (font choice is critical for the aesthetic).
2. Visual Style
• Aim for a creative, modern, and fresh look. Avoid outdated or generic stock imagery/layouts.
3. Imagery/Graphic Element (Artist's Choice)
You have creative freedom regarding the main graphic element.
• Option A (Photography): Use a photo of a white male American with a collared shirt. The imagery should convey success, focus, or professional development.
• Option B (Vector/Illustration): Use a modern vector graphic, illustration, or abstract design. This could be used to symbolize growth, connection, or a career path.
The choice of graphic element is yours, but it must support the overall modern and uncrowded aesthetic.

Requirements
Must have
• Partial listing .. is part of the Harbor Lantern Course

```html
<!DOCTYPE html>
<html lang="en">
<head>
<meta charset="utf-8">
<title>Skill Up, Salary Up – Upcoming KVL Courses</title>
<link rel="stylesheet" href="https://fonts.googleapis.com/css2?family=Bebas+Neue&family=Poppins:wght@400;500;600;700;800&display=swap">
<style>
  :root{
    --stage:#b3b3b3;
    --trim:#f1f2f4;
    --sky:#00aeef;
    --card-light:#12a4dc;
    --navy:#164686;
    --ink:#1b3f86;
    --tag-navy:#1a3d84;
    --tag-mid:#176bb0;
    --ring:#1a6aaa;
    --white:#ffffff;
  }
  *{box-sizing:border-box;margin:0;padding:0}
  html,body{width:908px;height:1200px;overflow:hidden}
  body{background:var(--stage);position:relative;font-family:"Poppins",sans-serif;color:var(--white)}
  .trim{position:absolute;left:82px;top:83px;width:744px;height:1035px;background:var(--trim)}
  .page{position:absolute;left:103px;top:103px;width:703px;height:993px;background:var(--sky);overflow:hidden}
  .page > *{position:absolute}

  .headline{left:37px;top:35px;color:var(--ink);font-weight:800;font-size:52px;line-height:45px;letter-spacing:-0.5px}
  .title{left:37px;top:128px;font-family:"Bebas Neue",sans-serif;font-size:86px;line-height:66px;color:var(--white)}

  .tag{height:23px;line-height:23px;padding:0 6px;border-radius:4px;font-size:13px;font-weight:500;color:var(--white);white-space:nowrap}
  .tag-audience{left:37px;top:279px;width:114px;background:var(--tag-navy)}
  .tag-format{left:155px;top:279px;width:159px;background:var(--tag-mid)}
  .tag-aid{left:37px;top:307px;width:185px;background:var(--tag-navy)}

  .portrait{left:391px;top:43px;width:274px;height:274px}

  .card{padding:0 22px;color:var(--white)}
  .card-light{background:var(--card-light);--tick-bg:var(--card-light)}
  .card-navy{background:var(--navy);--tick-bg:var(--navy)}
  .card h3{font-size:17px;font-weight:500;line-height:21px;white-space:nowrap}
  .sub{font-size:12px;font-weight:600;line-height:15px}
  .dur{font-size:15px;font-weight:700;line-height:15px}
  .ticks{list-style:none;font-size:11px;line-height:17.4px}
  .ticks li{position:relative;padding-left:11px;white-space:nowrap}
  .ticks li::before{content:"";position:absolute;left:0;top:4.4px;width:8px;height:8px;border-radius:50%;background:var(--white)}
  .ticks li::after{content:"";position:absolute;left:2.6px;top:6px;width:2px;height:3.6px;border:solid var(--tick-bg);border-width:0 1.3px 1.3px 0;transform:rotate(45deg)}
  .cols-wide{display:grid;grid-template-columns:126px 1fr}
  .cols-narrow{display:grid;grid-template-columns:78px 1fr}

  .card-harbor{left:37px;top:351px;width:303px;height:311px;padding-top:10px}
  .card-harbor .ticks:first-of-type{margin-top:0}
  .card-harbor .dur{margin-top:6px}
  .listing-label{margin-top:21px;font-size:16px;font-weight:600;line-height:20px}

  .card-ledger{left:353px;top:351px;width:312px;height:169px;padding-top:10px}
  .card-ledger .sub{margin-top:5px}
  .card-ledger .ticks{margin-top:5px}
  .card-ledger .dur{margin-top:4.5px}

  .card-it{left:353px;top:532px;width:312px;height:171px;padding-top:8px}
  .card-it .sub{margin-top:3.5px}
  .card-it .sub + .sub{margin-top:5px}
  .card-it .ticks{margin-top:2px}
  .card-it .dur{margin-top:8.5px}

  .card-soft{left:37px;top:673px;width:303px;height:209px;padding-top:16px}
  .card-soft .sub{margin-top:0.5px}
  .card-soft .sub.jobs{margin-top:9px}
  .card-soft .ticks{margin-top:1px}
  .card-soft .sub.degree{margin-top:7px}
  .card-soft .dur{margin-top:5px;font-size:16px;line-height:17px}

  .card-office{left:353px;top:715px;width:312px;height:167px;padding-top:8px}
  .card-office .sub{margin-top:6.5px}
  .card-office .ticks{margin-top:4px}
  .card-office .sub.lab{margin-top:4.5px}
  .card-office .dur{margin-top:8px}

  .footer{left:0;top:909px;width:703px;height:84px;background:var(--card-light);display:flex;align-items:center;justify-content:center;font-size:27px;font-weight:600;letter-spacing:4.5px;color:var(--white)}
</style>
</head>
<body>
  <div class="trim"></div>
  <main class="page">
    <h1 class="headline">SKILL UP,<br>SALARY UP</h1>
    <h2 class="title">UPCOMING<br>KVL COURSES</h2>

    <div class="tag tag-audience">MEN &amp; WOMEN</div>
    <div class="tag tag-format">IN-PERSON &amp; REMOTE</div>
    <div class="tag tag-aid">PARTIAL SCHOLORASHIPS</div>

    <svg class="portrait" viewBox="0 0 274 274" role="img" aria-label="Photo of a smiling young student in a checked collared shirt holding a laptop and backpack strap">
      <defs>
        <linearGradient id="portraitFill" x1="0" y1="0" x2="0" y2="1">
          <stop offset="0" stop-color="#e9ebee"/>
          <stop offset="1" stop-color="#9fb6d3"/>
        </linearGradient>
      </defs>
      <circle cx="137" cy="137" r="130.5" fill="none" stroke="var(--ring)" stroke-width="13"/>
      <circle cx="137" cy="137" r="124" fill="url(#portraitFill)"/>
    </svg>

    <section class="card card-light card-harbor">
      <h3>Harbor Lantern Course</h3>
      <h3>Business Skills &amp; Knowledge to:</h3>
      <ul class="ticks">
        <li>Impress your interviewer</li>
        <li>Maximize Income</li>
        <li>Start / Run Your Business</li>
      </ul>
      <p class="dur">4-5 MONTHS<br>NOV&nbsp; 2025</p>
      <p class="listing-label">PARTIAL LISTING</p>
      <ul class="ticks cols-wide">
        <li>Computers</li><li>Communication</li>
        <li>Marketing</li><li>LedgerLine</li>
        <li>Sales</li><li>Investments</li>
        <li>Finance</li><li>Real Estate</li>
        <li>Healthcare</li><li>Accounting</li>
        <li>Business Strategy</li>
      </ul>
    </section>

    <section class="card card-light card-ledger">
      <h3>Bookkeeping LedgerLine</h3>
      <p class="sub">Train for a quality job<br>Manage your own books</p>
      <ul class="ticks">
        <li>Finance Management</li>
        <li>Customer &amp; Vendor Mgmt.</li>
        <li>Advanced Tools</li>
      </ul>
      <p class="dur">5 WEEKS<br>NOV&nbsp; 2025</p>
    </section>

    <section class="card card-navy card-it">
      <h3>IT Desktop &amp; Networking Support</h3>
      <p class="sub">#2 Best Job<br>National Careers Review 2025</p>
      <p class="sub">Masters IT:</p>
      <ul class="ticks cols-narrow">
        <li>Desktop OS</li><li>Servers</li>
        <li>Networks</li><li>Cloud</li>
      </ul>
      <p class="dur">7 MONTHS<br>Dec 2025</p>
    </section>

    <section class="card card-navy card-soft">
      <h3>Software, Web &amp; Apps</h3>
      <p class="sub"># 2 Best Tech Job<br>National Careers Review 2025</p>
      <p class="sub jobs">Job Opportunities</p>
      <ul class="ticks">
        <li>Computer Programmer</li>
        <li>Software Developer/Mobile</li>
        <li>Engineer Developer (Apps</li>
      </ul>
      <p class="sub degree">Optional: Bachelors in Prog. &amp; Tech.</p>
      <p class="dur">NOV&nbsp; 2025</p>
    </section>

    <section class="card card-light card-office">
      <h3>Bright Office- Computers</h3>
      <p class="sub">The New&nbsp;&nbsp; Job Prerequisite</p>
      <ul class="ticks cols-narrow">
        <li>CalcGrid</li><li>MailDock</li>
        <li>WriteDesk</li><li>DeckMaker</li>
      </ul>
      <p class="sub lab">Computer lab available to practice</p>
      <p class="dur">5 WEEKS<br>DEC 2025</p>
    </section>

    <footer class="footer">FOOTER BLEED 1 INCH</footer>
  </main>
</body>
</html>
```